Web Design for Financial Consulting Company

We need a website design for a financial consulting company "Kelvane Consulting". We build financial models, scenario analysis, handle the budgeting process and provide temporary staffing. I have over 10 years of experience. My Excel expertise and analytical savvy has saved clients over $17 million in profit.

Target Market(s)

Small to medium businesses

Industry/Entity Type

Financial Consulting

Number of Pages Required

4 page

Requirements
Must have
• Professional looking
Nice to have
• A little futuristic looking

```html
<!DOCTYPE html>
<html lang="en">
<head>
<meta charset="utf-8">
<title>Kelvane Consulting – Web Design</title>
<link href="https://fonts.googleapis.com/css2?family=DM+Sans:wght@400;500;700&display=swap" rel="stylesheet">
<style>
  :root{
    --navy:#002c46;
    --blue:#024268;
    --sky:#01aef7;
    --board:#eceff2;
    --white:#ffffff;
    --band:#f6f8fa;
    --text:#5d6b78;
    --rule:#dfe4e9;
  }
  *{margin:0;padding:0;box-sizing:border-box}
  html,body{width:1200px;height:2429px;overflow:hidden}
  body{background:var(--board);font-family:"DM Sans",sans-serif;color:var(--blue);position:relative}
  .abs{position:absolute}

  /* board header */
  .brand{left:203px;top:134px;display:flex;align-items:center;gap:10px}
  .brand-square{width:32px;height:32px;border:3px solid var(--sky)}
  .brand-name{font-size:24px;font-weight:700;color:var(--blue);letter-spacing:.5px}
  .board-label{font-size:26px;font-weight:400;color:var(--navy)}
  .fonts-label{left:611px;top:100px}
  .fonts-value{left:611px;top:148px;font-size:15px;color:#6b7580}
  .colors-label{left:889px;top:100px}
  .swatch{top:137px;width:42px;height:42px;border-radius:50%}
  .swatch-code{top:187px;width:60px;text-align:center;font-size:9px;color:#3b4652}

  /* site */
  .site{left:222px;top:272px;width:792px;height:2054px;background:var(--white);overflow:hidden}
  .nav{position:absolute;left:0;top:0;width:792px;height:40px;background:var(--white)}
  .nav-square{position:absolute;left:0;top:0;width:40px;height:40px;background:var(--blue)}
  .nav-square span{position:absolute;left:11px;top:11px;width:18px;height:18px;border:1.5px solid var(--white)}
  .nav-brand{position:absolute;left:48px;top:11px;font-size:14px;font-weight:700;color:var(--blue)}
  .nav-links{position:absolute;left:433px;top:14px;display:flex;gap:27px;font-size:8px;color:var(--navy)}
  .nav-phone{position:absolute;left:591px;top:9px;width:22px;height:22px;border-radius:50%;background:var(--sky)}
  .nav-mail{position:absolute;left:627px;top:15px;font-size:7px;color:#6d7a86}

  .hero{position:absolute;left:39px;top:39px;width:753px;height:372px;
    background:radial-gradient(ellipse at 58% 45%,#1f7fc4 0%,#0b4c86 28%,#05284e 55%,#010f22 85%)}
  .hero-title{position:absolute;left:59px;top:224px;font-size:28px;line-height:30px;font-weight:400;color:var(--white)}
  .hero-title em{font-style:normal;color:#4fb3e8}
  .hero-arrow{position:absolute;left:618px;top:231px;width:74px;height:74px;border-radius:50%;border:1px solid #2f79ad}

  .stat{position:absolute;top:466px;width:150px;text-align:center}
  .stat-num{font-size:26px;font-weight:400;color:var(--blue);line-height:30px}
  .stat-label{font-size:8px;color:var(--sky);margin-top:2px}
  .stat-slash{position:absolute;top:471px;width:1px;height:38px;background:var(--sky);transform:rotate(25deg)}

  .section-title{font-size:23px;line-height:26px;font-weight:400;color:var(--blue)}
  .body-copy{font-size:8px;line-height:14px;color:var(--text)}
  .photo{position:absolute}

  .services{position:absolute;left:0;top:1041px;width:792px;height:465px;background:var(--band)}
  .service{position:absolute;left:383px;width:349px;height:91px;border-bottom:1px solid var(--rule)}
  .service-icon{position:absolute;left:0;top:4px;width:30px;height:34px}
  .service-title{position:absolute;left:52px;top:0;font-size:18px;line-height:20px;color:var(--blue)}
  .service-desc{position:absolute;left:224px;top:2px;width:128px;font-size:7px;line-height:13px;color:#7a8794}
  .service-more{position:absolute;left:224px;top:49px;font-size:7px;color:var(--blue);display:flex;align-items:center;gap:5px}
  .service-more::before{content:"";width:14px;height:1px;background:var(--sky)}

  .contact-band{position:absolute;left:0;top:1506px;width:792px;height:275px;
    background:linear-gradient(120deg,#0a2c52 0%,#0d4f88 40%,#1b78c0 58%,#0b3a6a 78%,#071d3a 100%)}
  .contact-circle{position:absolute;left:648px;top:131px;width:84px;height:84px;border-radius:50%;border:1px solid #7fa9cc;
    display:flex;align-items:center;justify-content:center;font-size:8px;font-weight:500;color:var(--white)}

  .footer{position:absolute;left:0;top:1781px;width:792px;height:273px;background:var(--navy)}
  .footer-brand{position:absolute;left:60px;top:58px;display:flex;align-items:center;gap:6px}
  .footer-brand span{width:16px;height:16px;border:2px solid var(--sky)}
  .footer-brand b{font-size:13px;font-weight:700;color:var(--white)}
  .footer-tag{position:absolute;left:352px;top:55px;width:400px;font-size:13px;line-height:17px;font-weight:500;color:var(--white)}
  .footer-col{position:absolute;top:127px}
  .footer-head{font-size:9px;color:var(--sky);margin-bottom:8px}
  .footer-line{font-size:7px;line-height:16px;color:var(--white)}
  .socials{display:flex;gap:6px}
  .socials span{width:17px;height:17px;border-radius:50%;background:var(--sky)}
  .footer-small{position:absolute;top:204px;font-size:6px;color:#8ea6bb}
</style>
</head>
<body>

<!-- board header -->
<div class="abs brand"><span class="brand-square"></span><span class="brand-name">Kelvane Consulting</span></div>
<div class="abs board-label fonts-label">Fonts:</div>
<div class="abs fonts-value">DM Sans</div>
<div class="abs board-label colors-label">Colors:</div>
<div class="abs swatch" style="left:890px;background:var(--navy)"></div>
<div class="abs swatch" style="left:941px;background:var(--blue)"></div>
<div class="abs swatch" style="left:993px;background:var(--sky)"></div>
<div class="abs swatch-code" style="left:881px">#002c46</div>
<div class="abs swatch-code" style="left:932px">#024268</div>
<div class="abs swatch-code" style="left:984px">#01aef7</div>

<!-- website -->
<main class="abs site">
  <header class="nav">
    <div class="nav-square"><span></span></div>
    <div class="nav-brand">Kelvane Consulting</div>
    <nav class="nav-links"><span>About</span><span>Services</span><span>Contact</span></nav>
    <div class="nav-phone">
      <svg width="22" height="22" viewBox="0 0 22 22"><path d="M8 6.5c.6 2.9 2.5 5.6 5.4 7.3l1.4-1.3 2 1.1-.6 1.8c-4.5-.3-8.3-4.2-8.6-8.7l1.8-.6z" fill="#fff"/></svg>
    </div>
    <div class="nav-mail">info@kelvaneconsulting.com</div>
  </header>

  <section class="hero" role="img" aria-label="Hand touching a tablet with a glowing rising financial chart">
    <h1 class="hero-title">Helping Your<br>Finance Team &amp;<br><em>Increasing Profit</em></h1>
    <div class="hero-arrow">
      <svg width="74" height="74" viewBox="0 0 74 74"><path d="M30 45 L44 31 M33 30 H44 V41" stroke="#fff" stroke-width="2" fill="none"/></svg>
    </div>
  </section>

  <div class="stat" style="left:24px"><div class="stat-num">30+</div><div class="stat-label">Years of Experience</div></div>
  <div class="stat-slash" style="left:202px"></div>
  <div class="stat" style="left:223px"><div class="stat-num">19786</div><div class="stat-label">Happy Clients</div></div>
  <div class="stat-slash" style="left:394px"></div>
  <div class="stat" style="left:422px"><div class="stat-num">456</div><div class="stat-label">Completed Projects</div></div>
  <div class="stat-slash" style="left:600px"></div>
  <div class="stat" style="left:622px"><div class="stat-num">23786</div><div class="stat-label">Happy Clients</div></div>

  <h2 class="abs section-title" style="left:60px;top:563px">Your Trusted<br>Financial Partner</h2>
  <p class="abs body-copy" style="left:383px;top:566px;width:352px">An experienced Finance professional who develops strategic financial plans, provides insightfulanalysis, and supports decision-making.</p>
  <div class="photo" role="img" aria-label="Business team in silhouette discussing reports in a bright office" style="left:60px;top:631px;width:303px;height:258px;background:linear-gradient(160deg,#b9d3ec 0%,#5f8fc2 40%,#1c3f6e 70%,#8fb4da 100%)"></div>
  <p class="abs body-copy" style="left:60px;top:903px;width:305px">With over 10 years of experience, I have successfully increased the profitability for clients by $17M. Through my meticulous analysis of market trends and competitor dynamics, I have guided clients towards informed business decisions &amp; enabling them to stay ahead in a competition</p>
  <div class="photo" role="img" aria-label="Glass office towers seen from below" style="left:383px;top:611px;width:187px;height:185px;background:linear-gradient(135deg,#3d4b5c 0%,#a9b9c9 45%,#e6eef5 60%,#2f6fa8 100%)"></div>
  <div class="photo" role="img" aria-label="Hands reviewing financial charts on paper, tablet and laptop" style="left:383px;top:816px;width:349px;height:164px;background:linear-gradient(110deg,#2b3441 0%,#c9d2dc 35%,#eef1f4 60%,#5f7388 100%)"></div>

  <section class="services">
    <h2 class="abs section-title" style="left:60px;top:69px">Services<br>We Offer</h2>

    <div class="service" style="top:58px">
      <svg class="service-icon" viewBox="0 0 30 34" fill="none" stroke="#024268" stroke-width="1.3"><rect x="2" y="2" width="20" height="28" rx="1"/><path d="M6 9h12M6 14h8M6 19h6"/><circle cx="21" cy="22" r="6" stroke="#01aef7"/></svg>
      <div class="service-title">Financial Models<br>&amp; Projects</div>
      <div class="service-desc">Financial analysis, scenario modeling, pricing analysis, projects and much more than that.</div>
      <div class="service-more">Discover More</div>
    </div>
    <div class="service" style="top:149px">
      <svg class="service-icon" viewBox="0 0 30 34" fill="none" stroke="#024268" stroke-width="1.3"><path d="M3 30V20h5v10M11 30V16h5v14M19 30V12h5v18"/><path d="M3 12l8-5 5 3 10-7" stroke="#01aef7"/></svg>
      <div class="service-title">Budgeting<br>Process</div>
      <div class="service-desc">Building budgets from scratch, revamping current process to be more robust and scalable.</div>
      <div class="service-more">Discover More</div>
    </div>
    <div class="service" style="top:240px">
      <svg class="service-icon" viewBox="0 0 30 34" fill="none" stroke="#024268" stroke-width="1.3"><circle cx="15" cy="8" r="4"/><circle cx="6" cy="22" r="3"/><circle cx="24" cy="22" r="3"/><path d="M1 31c0-3 2-5 5-5s5 2 5 5M19 31c0-3 2-5 5-5s5 2 5 5"/><circle cx="15" cy="22" r="2" fill="#01aef7" stroke="none"/></svg>
      <div class="service-title">Temporary<br>Staffing</div>
      <div class="service-desc">Years of Financial Planning &amp; Analysis experience across multiple industries can help temporary staffing needs.</div>
      <div class="service-more">Discover More</div>
    </div>
    <div class="service" style="top:331px">
      <svg class="service-icon" viewBox="0 0 30 34" fill="none" stroke="#024268" stroke-width="1.3"><circle cx="15" cy="16" r="11" stroke-dasharray="3 2"/><circle cx="15" cy="16" r="6" stroke="#01aef7"/><path d="M11 29h8M12 32h6"/></svg>
      <div class="service-title">Process<br>Improvements</div>
      <div class="service-desc">Month end close, reporting, budgeting</div>
      <div class="service-more">Discover More</div>
    </div>
  </section>

  <section class="contact-band" role="img" aria-label="Person working on a laptop and tablet with glowing network lines">
    <div class="contact-circle">Contact Us</div>
  </section>

  <footer class="footer">
    <div class="footer-brand"><span></span><b>Kelvane Consulting</b></div>
    <p class="footer-tag">We Believe That by Empowering Ourselves, We Can Empower the World Around Us.</p>
    <div class="footer-col" style="left:352px">
      <div class="footer-head">Contact</div>
      <div class="footer-line">info@kelvaneconsulting.com<br>+1 555 014 2290</div>
    </div>
    <div class="footer-col" style="left:521px">
      <div class="footer-head">Address</div>
      <div class="footer-line">info@kelvaneconsulting.com<br>+1 555 014 2290</div>
    </div>
    <div class="footer-col" style="left:689px">
      <div class="footer-head">Socials</div>
      <div class="socials"><span></span><span></span></div>
    </div>
    <div class="footer-small" style="left:352px">Terms and Conditions</div>
    <div class="footer-small" style="left:521px">Privacy Policy</div>
    <div class="footer-small" style="left:671px">© 2023 - Kelvane</div>
  </footer>
</main>

</body>
</html>
```